New Architectural Firm Business Cards

New Business card to compliment previous pixel forum logo (attached). Please design a business card that is simple, modern, creative....please do not use "symbols", simply the logo and associated graphics/text. The front should contain name/address/phone/email/web address (with graphics).....back should be 100% graphic design using the logo somehow. Hoping for a two color (black and yellow) design. full bleed design, no borders

Target Market(s)

Commercial Architecture Clients

Industry/Entity Type

Architecture

Contact Information for Business Card

Please design a business card that is simple, modern, creative....please do not use "symbols", simply the logo and associated graphics/text. The front should contain name/address/phone/email/web address (with graphics).....back should be 100% graphic design using the logo somehow

Font styles to use
Sans Serif

Colors
FFF300
FFF600
FEFA6F
FFFEC7
FFFEE8

Requirements
Must have
• Clean, Modern Design
Should not have
• Stock images or "icons"

```html
<!DOCTYPE html>
<html lang="en">
<head>
<meta charset="utf-8">
<title>pixel forum — business cards</title>
<link rel="stylesheet" href="https://fonts.googleapis.com/css2?family=Arimo:wght@400;700&display=swap">
<style>
  :root {
    --ink: #000000;
    --yellow: #f8c614;
    --stage: #1c1c1c;
    --light: #e9e9e9;
  }
  * { margin: 0; padding: 0; box-sizing: border-box; }
  html, body { width: 1200px; height: 1015px; overflow: hidden; }
  body {
    background: var(--stage);
    font-family: "Arimo", Arial, sans-serif;
    position: relative;
  }
  .card {
    position: absolute;
    width: 600px;
    height: 343px;
  }
  .card--back {
    left: 100px; top: 110px;
    background: var(--ink);
    display: flex; align-items: center; justify-content: center;
  }
  .card--front {
    left: 500px; top: 540px;
    background: var(--yellow);
    color: var(--ink);
    display: flex; align-items: center;
  }
  .brand {
    display: flex; align-items: center; gap: 14px;
    font-weight: 700;
    letter-spacing: 1px;
    text-transform: uppercase;
  }
  .brand__square { width: 34px; height: 34px; }
  .card--back .brand { color: var(--yellow); font-size: 38px; }
  .card--back .brand__square { background: var(--yellow); }
  .card--front .brand { font-size: 30px; color: var(--ink); }
  .card--front .brand__square { background: var(--ink); width: 28px; height: 28px; }
  .front__logo { width: 300px; display: flex; justify-content: center; }
  .divider { width: 1px; height: 200px; background: var(--ink); }
  .contact { padding-left: 30px; font-size: 14px; line-height: 1.35; }
  .contact__name { font-size: 19px; font-weight: 700; text-transform: uppercase; }
  .contact__role { margin-bottom: 16px; }
  .contact__list { list-style: none; margin-bottom: 14px; }
  .contact__list li { display: flex; align-items: center; gap: 8px; }
  .contact__list svg { width: 13px; height: 13px; flex: none; }
</style>
</head>
<body>
  <section class="card card--back">
    <div class="brand"><span class="brand__square"></span>pixel forum</div>
  </section>

  <section class="card card--front">
    <div class="front__logo">
      <div class="brand"><span class="brand__square"></span>pixel forum</div>
    </div>
    <div class="divider"></div>
    <div class="contact">
      <p class="contact__name">Daniel Reeves</p>
      <p class="contact__role">Managing Director</p>
      <ul class="contact__list">
        <li>
          <svg viewBox="0 0 16 16"><path d="M3 1l3 3-2 2c1 2 3 4 5 5l2-2 3 3-2 2C7 14 2 9 1 3z" fill="currentColor"/></svg>
          055-210 987 340
        </li>
        <li>
          <svg viewBox="0 0 16 16"><rect x="1" y="3" width="14" height="10" fill="currentColor"/><path d="M1 3l7 6 7-6" fill="none" stroke="#f8c614" stroke-width="1.4"/></svg>
          hello@pixelforum.net
        </li>
        <li>
          <svg viewBox="0 0 16 16"><circle cx="8" cy="8" r="6.5" fill="none" stroke="currentColor" stroke-width="1.6"/><path d="M1.5 8h13M8 1.5c-3 3.5-3 9.5 0 13M8 1.5c3 3.5 3 9.5 0 13" fill="none" stroke="currentColor" stroke-width="1.2"/></svg>
          www.pixelforum.net
        </li>
      </ul>
      <p class="contact__address">17, Harbour Row Studio<br>30218, Northland</p>
    </div>
  </section>
</body>
</html>
```